New iOS App design for Boston Startup

We are looking for a new app design for our iPhone app. The current app's design feels outdated and we like to add lots of new functionality and a new navigation as well. A complete overhaul therefore!
We want you to design 5 screens that will have changed the most. The complete wireframes of these 5 pages are attached in the requirements document.
Once the winning design is selected we will award the winner with the designing all other screens (40-50 screens based on the same design). This will be a separate project worth $1000. The winning designer can get more follow up work if both sides are happy about the cooperation.
We will give feedback as soon as the first screen has been uploaded for review. Final decision will be made only after all 5 screens are finished.
We hope you give it your best!
Note: will only communicate through ArtVantle (no skype),
Updates
Reason: Want to give designers a chance to submit their designs as I understand from some, the deadline is too close.
I have raised the award and introduced a 2nd price as well to make it worth your time. I hope you give it your best shot.
Reason: A few of you have asked for an extension of the deadline as time is running out. I will extend by one day. Tell me if you need more.
Industry/Entity Type
Startup
Requirements
Must have
- At least 1 screen before we can give you feedback.
Nice to have
- multiple options of 1 screen to get to a desirable design

```html
<!DOCTYPE html>
<html lang="en">
<head>
<meta charset="utf-8">
<title>Home – Study Dashboard</title>
<link rel="stylesheet" href="https://fonts.googleapis.com/css2?family=Roboto:wght@400;500;700&display=swap">
<style>
  :root {
    --navy: #0c3350;
    --navy-line: #1b4666;
    --page: #f4f4f2;
    --white: #ffffff;
    --ink: #0c3350;
    --black: #111111;
    --green: #3f7d12;
    --red: #ef7d78;
    --orange: #f68a33;
    --muted: #c6c6c6;
    --tab-active: #00b3ef;
  }
  * { box-sizing: border-box; margin: 0; padding: 0; }
  html, body { width: 800px; height: 1200px; overflow: hidden; }
  body {
    position: relative;
    background: var(--page);
    font-family: "Roboto", "Helvetica Neue", Arial, sans-serif;
    color: var(--ink);
  }

  /* Top bar */
  .app-header {
    position: absolute; left: 0; top: 0; width: 800px; height: 160px;
    background: var(--navy); color: var(--white);
  }
  .status-bar {
    position: absolute; left: 0; top: 0; width: 800px; height: 50px;
    font-size: 27px; font-weight: 400;
  }
  .status-bar .carrier { position: absolute; left: 6px; top: 9px; display: flex; align-items: center; gap: 6px; }
  .status-bar .clock { position: absolute; left: 0; width: 800px; top: 9px; text-align: center; font-weight: 500; }
  .status-bar .right { position: absolute; right: 8px; top: 9px; display: flex; align-items: center; gap: 10px; }
  .menu-toggle { position: absolute; left: 30px; top: 85px; }
  .welcome {
    position: absolute; left: 0; width: 800px; top: 78px; text-align: center;
    font-size: 41px; font-weight: 700; padding-left: 30px;
  }

  /* Score card */
  .score-card {
    position: absolute; left: 30px; top: 178px; width: 170px; height: 162px;
    background: var(--white); border-radius: 6px; overflow: hidden; text-align: center;
  }
  .score-card .label {
    height: 46px; background: var(--navy); color: var(--white);
    font-size: 33px; font-weight: 500; line-height: 46px; letter-spacing: 1px;
  }
  .score-card .value { font-size: 75px; font-weight: 700; line-height: 80px; margin-top: 0; }
  .score-card .delta { font-size: 24px; color: var(--red); line-height: 26px; }

  /* Weekly stats */
  .week-stats {
    position: absolute; left: 229px; top: 181px; width: 536px; height: 101px;
    border: 2px solid var(--navy); border-radius: 6px; overflow: hidden; background: var(--white);
    display: flex;
  }
  .stat { flex: 1; display: flex; flex-direction: column; border-left: 2px solid var(--navy); }
  .stat:first-child { border-left: 0; }
  .stat .figure {
    height: 66px; display: flex; align-items: center; justify-content: center;
    font-size: 38px; color: var(--black);
  }
  .stat .gain { color: var(--green); font-size: 25px; margin-left: 2px; display: flex; align-items: center; }
  .stat .caption {
    flex: 1; background: var(--navy); color: var(--white); text-align: center;
    font-size: 27px; line-height: 31px; border-left: 2px solid var(--navy-line);
  }
  .stat:first-child .caption { border-left: 0; }
  .week-switch {
    position: absolute; left: 238px; top: 304px; width: 520px; height: 36px;
    display: flex; align-items: center; justify-content: space-between;
  }
  .week-switch .period { font-size: 26px; font-weight: 700; letter-spacing: 0.5px; }

  /* Action buttons */
  .btn {
    position: absolute; background: var(--navy); color: var(--white); border-radius: 6px;
    display: flex; align-items: center; justify-content: center; gap: 18px;
  }
  .btn-analytics { left: 32px; top: 415px; width: 350px; height: 85px; font-size: 35px; font-weight: 500; }
  .btn-overview { left: 418px; top: 415px; width: 350px; height: 85px; font-size: 30px; font-weight: 500; gap: 14px; }

  .countdown {
    position: absolute; left: 225px; top: 574px; width: 350px; height: 85px;
    background: var(--orange); color: var(--white); border-radius: 6px;
    display: flex; align-items: center; justify-content: center; gap: 12px; font-size: 32px; font-weight: 500;
  }
  .countdown .days { font-size: 41px; font-weight: 700; }

  .up-next {
    position: absolute; left: 221px; top: 703px; width: 359px;
    display: flex; align-items: center; gap: 14px; color: var(--muted); font-size: 26px;
  }
  .up-next .rule { flex: 1; height: 2px; background: #d9d9d9; }

  .btn-lesson { left: 250px; top: 773px; width: 300px; height: 76px; font-size: 36px; font-weight: 500; border-radius: 5px; }

  /* Tab bar */
  .tab-bar {
    position: absolute; left: 0; top: 1078px; width: 800px; height: 122px; background: var(--navy);
  }
  .tab {
    position: absolute; top: 0; width: 150px; height: 122px; color: var(--white);
    display: flex; flex-direction: column; align-items: center; font-size: 24px; font-weight: 500;
  }
  .tab svg { margin-top: 14px; height: 72px; }
  .tab .tab-label { margin-top: 6px; }
  .tab.is-active { background: var(--tab-active); top: -9px; height: 131px; }
  .tab.is-active svg { margin-top: 23px; }
</style>
</head>
<body>

<header class="app-header">
  <div class="status-bar">
    <div class="carrier">
      <svg width="78" height="16" viewBox="0 0 78 16"><g fill="#fff"><circle cx="7" cy="8" r="6.5"/><circle cx="22" cy="8" r="6.5"/><circle cx="37" cy="8" r="6.5"/></g><g fill="none" stroke="#fff" stroke-width="1.5"><circle cx="52" cy="8" r="6"/><circle cx="67" cy="8" r="6"/></g></svg>
      <span>Nuvell</span>
      <svg width="30" height="22" viewBox="0 0 30 22"><path d="M2 8 A18 18 0 0 1 28 8 M7 13 A11 11 0 0 1 23 13" fill="none" stroke="#fff" stroke-width="3.5" stroke-linecap="round"/><path d="M11 17 L15 21 L19 17 A6 6 0 0 0 11 17Z" fill="#fff"/></svg>
    </div>
    <div class="clock">23:12</div>
    <div class="right">
      <svg width="16" height="28" viewBox="0 0 16 28"><path d="M2 8 L14 20 L8 26 L8 2 L14 8 L2 20" fill="none" stroke="#fff" stroke-width="2.4"/></svg>
      <span>100%</span>
      <svg width="62" height="26" viewBox="0 0 62 26"><rect x="1.5" y="1.5" width="53" height="23" rx="4" fill="none" stroke="#fff" stroke-width="2.5"/><rect x="5" y="5" width="46" height="16" rx="2" fill="#fff"/><rect x="57" y="8" width="4" height="10" rx="1.5" fill="#fff"/></svg>
    </div>
  </div>
  <svg class="menu-toggle" width="52" height="40" viewBox="0 0 52 40"><g fill="#fff"><rect y="0" width="52" height="6" rx="2"/><rect y="17" width="52" height="6" rx="2"/><rect y="34" width="52" height="6" rx="2"/></g></svg>
  <h1 class="welcome">Welcome back, Maren</h1>
</header>

<section class="score-card">
  <div class="label">SCORE</div>
  <div class="value">650</div>
  <div class="delta">
    <svg width="12" height="18" viewBox="0 0 12 18"><path d="M6 1 V15 M1.5 10.5 L6 16 L10.5 10.5" fill="none" stroke="#ef7d78" stroke-width="2.4"/></svg>-18
  </div>
</section>

<section class="week-stats">
  <div class="stat">
    <div class="figure">34%<span class="gain"><svg width="16" height="26" viewBox="0 0 16 26"><path d="M8 25 V5 M2 11 L8 3 L14 11" fill="none" stroke="#3f7d12" stroke-width="4"/></svg>+10</span></div>
    <div class="caption">completion</div>
  </div>
  <div class="stat">
    <div class="figure">20<span class="gain"><svg width="16" height="26" viewBox="0 0 16 26"><path d="M8 25 V5 M2 11 L8 3 L14 11" fill="none" stroke="#3f7d12" stroke-width="4"/></svg>+3</span></div>
    <div class="caption">sessions</div>
  </div>
  <div class="stat">
    <div class="figure">18<span class="gain"><svg width="16" height="26" viewBox="0 0 16 26"><path d="M8 25 V5 M2 11 L8 3 L14 11" fill="none" stroke="#3f7d12" stroke-width="4"/></svg>+10</span></div>
    <div class="caption">min.</div>
  </div>
</section>

<nav class="week-switch">
  <svg width="16" height="24" viewBox="0 0 16 24"><path d="M13 2 L3 12 L13 22" fill="none" stroke="#0c3350" stroke-width="3.5"/></svg>
  <span class="period">THIS WEEK</span>
  <svg width="16" height="24" viewBox="0 0 16 24"><path d="M3 2 L13 12 L3 22" fill="none" stroke="#0c3350" stroke-width="3.5"/></svg>
</nav>

<div class="btn btn-analytics">
  <svg width="36" height="30" viewBox="0 0 36 30"><rect x="1.5" y="1.5" width="33" height="27" fill="none" stroke="#fff" stroke-width="2"/><path d="M5 23 L13 14 L19 19 L30 7" fill="none" stroke="#fff" stroke-width="2"/></svg>
  <span>Analytics</span>
</div>
<div class="btn btn-overview">
  <svg width="38" height="34" viewBox="0 0 38 34"><g fill="none" stroke="#fff" stroke-width="2"><circle cx="4" cy="4" r="2.5"/><circle cx="4" cy="17" r="2.5"/><circle cx="4" cy="30" r="2.5"/><path d="M12 4 H37 M12 17 H37 M12 30 H37"/></g></svg>
  <span>Course Overview</span>
</div>

<div class="countdown"><span class="days">33</span><span>Days until test</span></div>

<div class="up-next"><span class="rule"></span><span>Up Next</span><span class="rule"></span></div>

<div class="btn btn-lesson">SC-Lesson 3</div>

<nav class="tab-bar">
  <div class="tab" style="left:0">
    <svg width="60" height="72" viewBox="0 0 60 72"><g fill="none" stroke="#fff" stroke-width="3"><rect x="6" y="4" width="48" height="62"/><path d="M12 4 V66 M6 66 L10 70 H54"/></g></svg>
    <span class="tab-label">Theory</span>
  </div>
  <div class="tab" style="left:163px">
    <svg width="66" height="72" viewBox="0 0 66 72"><g fill="none" stroke="#fff" stroke-width="3" stroke-linejoin="round"><path d="M50 4 L62 16 L22 56 L6 64 L10 48 Z"/><path d="M44 10 L56 22 M10 48 L22 56"/></g></svg>
    <span class="tab-label">Practice</span>
  </div>
  <div class="tab is-active" style="left:325px">
    <svg width="64" height="62" viewBox="0 0 64 62"><path d="M32 2 L62 30 H54 V60 H40 V40 H24 V60 H10 V30 H2 Z" fill="#fff"/><rect x="44" y="6" width="8" height="16" fill="#fff"/></svg>
    <span class="tab-label">Home</span>
  </div>
  <div class="tab" style="left:487px">
    <svg width="60" height="72" viewBox="0 0 60 72"><g fill="none" stroke="#fff" stroke-width="3"><circle cx="30" cy="12" r="8"/><path d="M30 20 V48"/><rect x="4" y="48" width="52" height="14"/><path d="M12 48 V42 H22 V48"/></g></svg>
    <span class="tab-label">Games</span>
  </div>
  <div class="tab" style="left:650px">
    <svg width="56" height="72" viewBox="0 0 56 72"><g fill="none" stroke="#fff" stroke-width="3"><path d="M4 4 H38 L52 18 V68 H4 Z M38 4 V18 H52"/><path d="M12 28 H44 M12 36 H44 M12 44 H44 M12 52 H44 M12 60 H36"/></g></svg>
    <span class="tab-label">Test</span>
  </div>
</nav>

</body>
</html>
```